Coral Bay Grins Teeth Whitening Poster and possibly banner as well.

I need a poster and bamner put together for a kiosk stand in the mall we will be renting. I have some pictures. I want the poster to include one of the face and a nice holiday background. I would like it to say -Brighten Your Holiday Smile -Only $89 -Instant Results -Family Owned and Operated. I have a few pics to use or to use as ideas. Also to have our logo somewhere but small and a santa hat to be added to the shark

```html
<!DOCTYPE html>
<html lang="en">
<head>
<meta charset="utf-8">
<title>Coral Bay Grins – Holiday Poster</title>
<link rel="stylesheet" href="https://fonts.googleapis.com/css2?family=Libre+Baskerville:wght@700&family=Lobster+Two:ital,wght@1,700&family=Montserrat:wght@600;700&family=Oswald:wght@600&display=swap">
<style>
  :root {
    --page-bg: #e6e6e4;
    --poster-white: #fbfbfa;
    --wood-shade: #efefed;
    --brand-red: #b8172b;
    --sticker-red: #c8101f;
    --ink: #2b2b2b;
    --brand-blue: #1f4f74;
    --brand-dot: #4aa8d8;
    --snow-blue: #2aa3e3;
    --pine-dark: #2c4f27;
    --pine: #3f6d34;
    --gift-red: #d0231f;
    --gift-red-light: #e2412f;
    --ribbon: #f4ebe6;
    --pin-red: #d9161c;
    --pin-green: #3a9b35;
    --hair: #6b4a33;
    --skin: #e2b598;
    --skin-light: #f1dccf;
    --lip: #c9221f;
    --tooth: #fafafa;
  }
  * { box-sizing: border-box; margin: 0; padding: 0; }
  html, body { width: 1200px; height: 1200px; overflow: hidden; }
  body { background: var(--page-bg); position: relative; }

  .poster {
    position: absolute; left: 225px; top: 40px;
    width: 750px; height: 1120px; overflow: hidden;
    background: linear-gradient(160deg, var(--poster-white) 0%, var(--wood-shade) 55%, var(--poster-white) 100%);
  }

  /* holiday props: flat placeholders for photographed objects */
  .prop { position: absolute; }
  .gift { background: linear-gradient(135deg, var(--gift-red-light), var(--gift-red)); }
  .gift::after { content: ""; position: absolute; background: var(--ribbon); }
  .gift-top { right: 0; top: 0; width: 120px; height: 215px; border-bottom-left-radius: 6px; }
  .gift-top::after { left: 48px; top: 0; width: 22px; height: 100%; }
  .gift-left { left: 0; top: 300px; width: 60px; height: 160px; }
  .gift-left::after { left: 0; top: 70px; width: 100%; height: 20px; }

  .pine { border-radius: 999px;
    background: linear-gradient(90deg, var(--pine-dark), var(--pine)); }
  .pine-top { right: 105px; top: 26px; width: 150px; height: 26px; transform: rotate(-28deg); }
  .pine-right { right: -18px; top: 300px; width: 34px; height: 190px; transform: rotate(-8deg); }
  .pine-left-a { left: -30px; top: 228px; width: 120px; height: 24px; transform: rotate(6deg); }
  .pine-left-b { left: -14px; top: 560px; width: 30px; height: 220px; transform: rotate(-10deg); }
  .pine-left-c { left: -30px; top: 880px; width: 100px; height: 22px; transform: rotate(-35deg); }

  /* brand */
  .brand { position: absolute; left: 115px; top: 150px; display: flex; align-items: center; gap: 12px; }
  .brand-dot { width: 26px; height: 26px; border-radius: 50%; background: var(--brand-dot); }
  .brand-name { font-family: 'Montserrat', sans-serif; font-weight: 700; font-size: 24px; color: var(--brand-blue); }

  /* photo collage */
  .polaroid { position: absolute; background: #fff; padding: 12px;
    box-shadow: 0 6px 14px rgba(0,0,0,.22); }
  .polaroid .photo { width: 100%; height: 100%; }
  .pin { position: absolute; width: 18px; height: 18px; border-radius: 50%; top: -8px;
    box-shadow: 1px 2px 3px rgba(0,0,0,.35); }
  .pin-red { background: var(--pin-red); }
  .pin-green { background: var(--pin-green); }

  .snapshot-1 { left: 135px; top: 330px; width: 225px; height: 245px; transform: rotate(-12deg); }
  .snapshot-1 .photo { background: linear-gradient(90deg, var(--hair) 0 18%, var(--skin) 18% 78%, var(--skin-light) 78%); }
  .snapshot-2 { left: 370px; top: 345px; width: 220px; height: 215px; transform: rotate(8deg); }
  .snapshot-2 .photo { background: linear-gradient(180deg, var(--skin) 0 15%, var(--lip) 15% 35%, var(--tooth) 35% 55%, var(--lip) 55% 82%, var(--skin) 82%); }
  .snapshot-3 { left: 258px; top: 528px; width: 190px; height: 225px; transform: rotate(5deg); }
  .snapshot-3 .photo { background: linear-gradient(90deg, var(--hair) 0 20%, var(--skin) 20% 85%, var(--skin-light) 85%); }
  .snapshot-4 { left: 425px; top: 578px; width: 172px; height: 215px; transform: rotate(1deg); }
  .snapshot-4 .photo { background: linear-gradient(180deg, var(--skin-light) 0 20%, var(--skin) 20%); }

  .price-sticker { position: absolute; left: 150px; top: 612px; width: 140px; height: 140px;
    border-radius: 50%; background: var(--sticker-red); color: #fff; text-align: center;
    font-family: 'Oswald', sans-serif; font-weight: 600; line-height: 1;
    padding-top: 32px; transform: rotate(-6deg); box-shadow: 0 4px 10px rgba(0,0,0,.25); }
  .price-sticker .label { font-size: 36px; display: block; }
  .price-sticker .amount { font-size: 40px; display: block; }

  /* headline */
  .headline { position: absolute; left: 40px; right: 0; top: 858px; text-align: center; }
  .headline .kicker { font-family: 'Libre Baskerville', serif; font-weight: 700;
    font-size: 25px; color: var(--ink); letter-spacing: .5px; }
  .headline .title { font-family: 'Lobster Two', cursive; font-style: italic; font-weight: 700;
    font-size: 68px; color: var(--brand-red); margin-top: 2px; line-height: 1.05; }

  .perks { position: absolute; left: 95px; right: 40px; top: 1000px;
    display: flex; justify-content: space-between; list-style: none; }
  .perk { display: flex; align-items: center; gap: 8px;
    font-family: 'Montserrat', sans-serif; font-weight: 700; font-size: 17px;
    color: var(--ink); line-height: 1.25; text-transform: uppercase; }
  .perk svg { width: 34px; height: 34px; flex: none; }
</style>
</head>
<body>
<svg width="0" height="0" style="position:absolute">
  <defs>
    <symbol id="snowflake" viewBox="-20 -20 40 40">
      <g stroke="var(--snow-blue)" stroke-width="2.6" stroke-linecap="round" fill="none">
        <g id="arm"><line x1="0" y1="0" x2="0" y2="-17"/><polyline points="-5,-14 0,-9 5,-14"/><polyline points="-4,-8 0,-4 4,-8"/></g>
        <use href="#arm" transform="rotate(60)"/>
        <use href="#arm" transform="rotate(120)"/>
        <use href="#arm" transform="rotate(180)"/>
        <use href="#arm" transform="rotate(240)"/>
        <use href="#arm" transform="rotate(300)"/>
      </g>
    </symbol>
  </defs>
</svg>

<main class="poster">
  <div class="prop gift gift-top" role="img" aria-label="Red wrapped gift box with patterned ribbon"></div>
  <div class="prop gift gift-left" role="img" aria-label="Red wrapped gift with ribbon at the edge"></div>
  <div class="prop pine pine-top" role="img" aria-label="Pine branch"></div>
  <div class="prop pine pine-right" role="img" aria-label="Pine branch"></div>
  <div class="prop pine pine-left-a" role="img" aria-label="Pine branch"></div>
  <div class="prop pine pine-left-b" role="img" aria-label="Pine branches"></div>
  <div class="prop pine pine-left-c" role="img" aria-label="Pine branch"></div>

  <div class="brand">
    <span class="brand-dot"></span>
    <span class="brand-name">Coral Bay Grins</span>
  </div>

  <figure class="polaroid snapshot-1">
    <span class="pin pin-red" style="left:95px"></span>
    <div class="photo" role="img" aria-label="Smiling woman holding a glittering snowflake ornament"></div>
  </figure>
  <figure class="polaroid snapshot-2">
    <span class="pin pin-green" style="left:150px"></span>
    <div class="photo" role="img" aria-label="Close-up of a wide smile with red lips and white teeth"></div>
  </figure>
  <figure class="polaroid snapshot-3">
    <span class="pin pin-green" style="left:95px"></span>
    <div class="photo" role="img" aria-label="Excited woman with curly hair and a bright smile"></div>
  </figure>
  <figure class="polaroid snapshot-4">
    <span class="pin pin-red" style="left:60px"></span>
    <div class="photo" role="img" aria-label="Woman with a broad white smile"></div>
  </figure>

  <div class="price-sticker">
    <span class="label">ONLY</span>
    <span class="amount">$89</span>
  </div>

  <header class="headline">
    <p class="kicker">GIVE YOURSELF THE GIFT OF</p>
    <h1 class="title">A Coral Bay Grin?</h1>
  </header>

  <ul class="perks">
    <li class="perk"><svg><use href="#snowflake"/></svg><span>Brighten your<br>holiday smile</span></li>
    <li class="perk"><svg><use href="#snowflake"/></svg><span>Instant<br>results</span></li>
    <li class="perk"><svg><use href="#snowflake"/></svg><span>Family owned<br>and operated</span></li>
  </ul>
</main>
</body>
</html>
```